Plainly, Clover is both an activist blog and personal health journey.

I am launching a blog. Ostensibly, as a platform for me to blog about my 17 year survival of multiple cancers. The US government has obscured the truth about cannabis for far too long, and I see plainly clover as a platform, very Whitby-esque ... As in Cornelius Whitby, and plainly Neil. Here, it is my nom de guerre, Walter Sorrel. I want the look of the graphic splashes simple and clean and bold, ( Think Glen Marrow' design mentality) I have nothing to add or upload graphically, as I want you to interpret either your own views on the subject, or those of your interpretation of what other famous patriots ( yes, Walter Sorrel will be a famous patriots someday) like ( fill in the blank ), got another idea? I'm open. Communicate. If you have a completely different idea about how to get neatt, concise platform page with windows for a video intro, ... Bla bla bla

Reason: I have nothing I feel strongly about yet.

Target Market(s)

Admittedly, the helpless and hopeless, sick and dying, addicted and disenfranchised; all because it just doesn't have to be that way.

Industry/Entity Type

Government

Font styles to use
Serif
Sans Serif
Decorative
Script

Requirements
Must have
• So far, I remain uninspired. Am I missing some questions from any or all of you?
Nice to have
• Make suggestionsplease communicate your ideas
Should not have
• please communicate your ideas

```html
<!DOCTYPE html>
<html lang="en">
<head>
<meta charset="utf-8">
<title>Walter Sorrel — Blog Header</title>
<link rel="stylesheet" href="https://fonts.googleapis.com/css2?family=Cinzel:wght@600&family=Montserrat:wght@500&display=swap">
<style>
  :root {
    --ink: #0b0a06;
    --deep: #1c1407;
    --bronze: #6b4a12;
    --gold: #c8951e;
    --flare: #fff3b0;
    --title-gold: #f6d400;
    --band: rgba(4, 4, 2, 0.93);
  }
  html, body {
    margin: 0;
    padding: 0;
    width: 1200px;
    height: 547px;
    overflow: hidden;
    background: var(--ink);
  }
  .header {
    position: relative;
    width: 1200px;
    height: 547px;
    overflow: hidden;
  }
  .header__artwork {
    position: absolute;
    inset: 0;
    background:
      linear-gradient(118deg, transparent 40%, rgba(255, 243, 176, 0.55) 49%, rgba(255, 255, 240, 0.85) 51%, rgba(255, 243, 176, 0.45) 53%, transparent 62%),
      radial-gradient(ellipse 420px 300px at 560px 300px, rgba(255, 214, 80, 0.55), transparent 70%),
      radial-gradient(ellipse 380px 260px at 800px 70px, rgba(255, 200, 60, 0.45), transparent 70%),
      radial-gradient(ellipse 300px 200px at 700px 520px, rgba(255, 220, 120, 0.5), transparent 70%),
      linear-gradient(135deg, var(--deep) 0%, var(--bronze) 45%, var(--gold) 55%, var(--deep) 100%);
  }
  .header__nameplate {
    position: absolute;
    left: 0;
    top: 365px;
    width: 698px;
    height: 148px;
    background: var(--band);
    box-sizing: border-box;
    padding: 22px 0 0 40px;
  }
  .header__title {
    margin: 0;
    font-family: "Cinzel", "Trajan Pro", serif;
    font-weight: 600;
    font-size: 56px;
    line-height: 1;
    letter-spacing: 1px;
    color: var(--title-gold);
  }
  .header__subtitle {
    margin: 16px 0 0;
    font-family: "Montserrat", "Gotham", sans-serif;
    font-weight: 500;
    font-size: 25px;
    line-height: 1;
    color: var(--title-gold);
  }
</style>
</head>
<body>
  <header class="header">
    <div class="header__artwork" role="img" aria-label="Golden word-cloud artwork of boxed words such as community, honesty, trust, hope and relationship, crossed by a bright light flare"></div>
    <div class="header__nameplate">
      <h1 class="header__title">Walter Sorrel</h1>
      <p class="header__subtitle">Blog subheadline goes here</p>
    </div>
  </header>
</body>
</html>
```